Modernise Business Card

Our company has been operating for 10 years. With the start of the new decade we are looking to refresh our business card design. We manufacture a range of industrial product shipping to customers internationally. A copy of our current card, both sides, is attached. We are looking for a mature professional appearance.

```html
<!DOCTYPE html>
<html lang="en">
<head>
<meta charset="utf-8">
<title>Korvane Business Card</title>
<link href="https://fonts.googleapis.com/css2?family=Open+Sans:wght@300;400;600;700&display=swap" rel="stylesheet">
<style>
  :root {
    --backdrop: #bdbec2;
    --card-light: #dfe4e4;
    --brand-blue: #07aed5;
    --ink: #231f20;
    --white: #ffffff;
  }
  * { margin: 0; padding: 0; box-sizing: border-box; }
  html, body { width: 1200px; height: 900px; overflow: hidden; }
  body {
    background: var(--backdrop);
    font-family: "Open Sans", Arial, sans-serif;
    position: relative;
  }
  .card {
    position: absolute;
    left: 306px;
    width: 588px;
    height: 336px;
    overflow: hidden;
  }
  .card-front { top: 69px; background: var(--card-light); }
  .card-back { top: 497px; background: var(--brand-blue); }

  .front-wordmark {
    position: absolute;
    left: 0; right: 0;
    top: 128px;
    text-align: center;
    font-weight: 700;
    font-size: 66px;
    line-height: 80px;
    color: var(--brand-blue);
    letter-spacing: -1px;
  }
  .front-web {
    position: absolute;
    left: 0; right: 0;
    top: 263px;
    text-align: center;
    font-weight: 300;
    font-size: 18px;
    line-height: 24px;
    color: var(--ink);
  }

  .back-shapes { position: absolute; inset: 0; }

  .back-wordmark {
    position: absolute;
    left: 26px;
    top: 26px;
    font-weight: 700;
    font-size: 50px;
    line-height: 64px;
    color: var(--card-light);
    letter-spacing: -1px;
  }
  .service-list { list-style: none; position: absolute; left: 23px; top: 142px; }
  .service-list li {
    font-size: 20px;
    line-height: 41px;
    color: var(--white);
    font-weight: 400;
  }
  .contact-name {
    position: absolute;
    left: 329px;
    top: 20px;
    font-weight: 600;
    font-size: 24px;
    line-height: 30px;
    color: var(--card-light);
  }
  .contact-block {
    position: absolute;
    font-size: 16px;
    line-height: 21px;
    color: var(--card-light);
    font-weight: 400;
  }
  .contact-phones { left: 306px; top: 84px; }
  .contact-online { left: 282px; top: 167px; }
  .contact-address { left: 256px; top: 249px; }
</style>
</head>
<body>
  <section class="card card-front">
    <div class="front-wordmark">Korvane</div>
    <div class="front-web">www.korvanefittings.com</div>
  </section>

  <section class="card card-back">
    <svg class="back-shapes" width="588" height="336" viewBox="0 0 588 336">
      <polygon points="303,0 314,0 212,336 200,336" fill="var(--card-light)"/>
      <polygon points="283,65 588,65 588,77 279,77" fill="var(--card-light)"/>
      <polygon points="258,148 588,148 588,159 255,159" fill="var(--card-light)"/>
      <polygon points="233,229 588,229 588,241 230,241" fill="var(--card-light)"/>
    </svg>

    <div class="back-wordmark">Korvane</div>

    <ul class="service-list">
      <li>HYDRAULIC ADAPTERS</li>
      <li>AQUICK COUPLINGS</li>
      <li>HOUSE FITTINGS</li>
    </ul>

    <div class="contact-name">Alan Pierce</div>
    <div class="contact-block contact-phones">
      China: +86 155 2730 4619<br>
      Australia: +61 412 378 905
    </div>
    <div class="contact-block contact-online">
      Email: apierce@korvanefittings.com<br>
      Web: www.korvanefittings.com
    </div>
    <div class="contact-block contact-address">
      Address: 1208-3, Lianhe Tower<br>
      416 Qiming Road, Haishu District<br>
      Ningbo 315000 China
    </div>
  </section>
</body>
</html>
```